Sydney law firm, Prestwicks Solicitors, needs a flyer design!

We need a flyer design for our law firm which has been operating in Sydney for over 35 years. We want to send the flyer out to potential clients and also to existing clients to let them know the range of services that we provide. Our corporate colours are white, red and black and we would like these incorporated somewhat. The final design should be clean, modern and professional.

We would like the design to fit a double sided flyer approx. 210mm high x 100mm wide.

Industry/Entity Type

Law Firm

Font styles to use
Serif
Sans Serif

Colors
eb2026
ffffff

Requirements
Must have
• Details needed on the flyer are:
• Prestwicks Solicitors
• 3/82 Carradine Street, Liverpool, NSW 2170
• (02) 9418 3562
• www.prestwickssolicitors-example.com.au
• info@prestwickssolicitors-example.com.au
• Our areas of practice include:
• Property Law
• Conveyancing
• Leases
• Criminal Law
• Family Law
• Litigation and Dispute Resolution
• Company Law
• Wills and Estates
• Powers of Attorney and Guardianship
Should not have
• a picture of scales or a picture of a gavel

```html
<!DOCTYPE html>
<html lang="en">
<head>
<meta charset="utf-8">
<title>Prestwicks Solicitors – Flyer</title>
<link rel="stylesheet" href="https://fonts.googleapis.com/css2?family=Arimo:wght@400;700&family=Cormorant+Garamond:wght@500&display=swap">
<style>
  :root {
    --red: #c41a10;
    --red-bright: #eb2026;
    --black: #000000;
    --white: #ffffff;
    --stage: #3f2520;
    --steel-dark: #2f3b4c;
    --steel-mid: #7d8a9c;
    --steel-light: #d5dbe3;
    --stone-light: #e6e3de;
    --stone-mid: #b9b5ae;
  }
  * { box-sizing: border-box; margin: 0; padding: 0; }
  html, body { width: 1200px; height: 900px; overflow: hidden; }
  body {
    position: relative;
    background: var(--stage);
    font-family: "Arimo", Arial, sans-serif;
  }

  /* ---------- Front panel ---------- */
  .front {
    position: absolute; left: 0; top: 0; width: 437px; height: 900px;
    background: var(--red);
  }
  .front__photo {
    position: absolute; left: 0; top: 0; width: 437px; height: 532px;
    background: linear-gradient(100deg, var(--steel-dark) 0%, var(--steel-mid) 35%, var(--steel-light) 60%, var(--steel-mid) 80%, var(--steel-light) 100%);
  }
  .front__brand {
    position: absolute; left: 0; width: 437px; top: 412px;
    text-align: center;
    font-family: "Cormorant Garamond", Georgia, serif;
    font-weight: 500;
    color: #1a1a1a;
    line-height: 1;
  }
  .front__brand-name { display: block; font-size: 52px; letter-spacing: 1px; }
  .front__brand-sub { display: block; font-size: 24px; letter-spacing: 12px; margin-top: 14px; padding-left: 12px; }
  .front__contact {
    position: absolute; left: 0; top: 544px; width: 437px;
    text-align: center; color: var(--white);
  }
  .front__name { font-size: 26px; font-weight: 700; margin-bottom: 8px; }
  .front__line { font-size: 15px; line-height: 19px; }

  /* ---------- Back panel ---------- */
  .back {
    position: absolute; left: 455px; top: 0; width: 427px; height: 900px;
    background: linear-gradient(90deg, var(--stone-mid), var(--stone-light) 40%, var(--stone-mid) 100%);
    overflow: hidden;
  }
  .back__frame { position: absolute; left: 0; top: 0; }
  .back__brand {
    position: absolute; left: 22px; top: 40px;
    font-family: "Cormorant Garamond", Georgia, serif; font-weight: 500;
    font-size: 13px; color: #1a1a1a; line-height: 1.1; text-align: center;
  }
  .back__brand small { display: block; font-size: 6px; letter-spacing: 3px; }
  .back__title {
    position: absolute; left: 143px; top: 44px;
    color: var(--white); font-weight: 700; font-size: 17.5px;
  }
  .practice { position: absolute; left: 0; top: 0; width: 427px; height: 900px; list-style: none; }
  .practice__item {
    position: absolute; right: 96px; width: 260px;
    color: var(--white); font-size: 13px; line-height: 16px; text-align: right;
  }
  .practice__rule {
    position: absolute; left: 120px; width: 225px; height: 2px;
    background: linear-gradient(90deg, rgba(196,26,16,0), #6a1410 40%, var(--red-bright));
  }
  .practice__photo {
    position: absolute;
    border: 3px solid var(--red-bright);
    background: linear-gradient(135deg, #e8e8e8, #8a8a8a);
    transform: rotate(-30deg);
  }
</style>
</head>
<body>

<section class="front" aria-label="Flyer front">
  <div class="front__photo" role="img" aria-label="Photo of a lawyer in a suit with arms folded before courthouse columns"></div>
  <div class="front__brand">
    <span class="front__brand-name">PRESTWICKS</span>
    <span class="front__brand-sub">SOLICITORS</span>
  </div>
  <div class="front__contact">
    <p class="front__name">Prestwicks Solicitors</p>
    <p class="front__line">3/82 Carradine Street, Liverpool, NSW 2170</p>
    <p class="front__line">(02) 9418 3562</p>
    <p class="front__line">www.prestwickssolicitors-example.com.au</p>
    <p class="front__line">info@prestwickssolicitors-example.com.au</p>
  </div>
</section>

<section class="back" aria-label="Flyer back">
  <div role="img" aria-label="Photo of courthouse columns and stone steps" style="position:absolute;inset:0"></div>
  <svg class="back__frame" width="427" height="900" viewBox="0 0 427 900">
    <path d="M132 0 Q92 450 132 900 L427 900 L427 0 Z" fill="var(--red-bright)"/>
    <path d="M140 6 Q101 450 140 894 L421 894 L421 6 Z" fill="var(--black)"/>
  </svg>
  <div class="back__brand">PRESTWICKS<small>SOLICITORS</small></div>
  <h2 class="back__title">Our areas of practice include:</h2>

  <ul class="practice">
    <li class="practice__item" style="top:95px">Property Law</li>
    <li class="practice__rule" style="top:114px"></li>
    <li class="practice__photo" style="left:362px;top:83px;width:40px;height:40px" role="img" aria-label="Photo of a house under construction"></li>

    <li class="practice__item" style="top:156px">Conveyancing</li>
    <li class="practice__rule" style="top:174px"></li>
    <li class="practice__photo" style="left:353px;top:156px;width:58px;height:58px" role="img" aria-label="Photo of a suburban home"></li>

    <li class="practice__item" style="top:256px">Leases</li>
    <li class="practice__rule" style="top:272px"></li>
    <li class="practice__photo" style="left:353px;top:253px;width:58px;height:58px" role="img" aria-label="Photo of a business meeting"></li>

    <li class="practice__item" style="top:344px">Criminal Law</li>
    <li class="practice__rule" style="top:361px"></li>
    <li class="practice__photo" style="left:353px;top:339px;width:58px;height:58px" role="img" aria-label="Photo of people in discussion"></li>

    <li class="practice__item" style="top:430px">Family Law</li>
    <li class="practice__rule" style="top:449px"></li>
    <li class="practice__photo" style="left:359px;top:427px;width:46px;height:46px" role="img" aria-label="Photo of a family outdoors"></li>

    <li class="practice__item" style="top:498px">Litigation and Dispute Resolution</li>
    <li class="practice__rule" style="top:517px"></li>
    <li class="practice__photo" style="left:359px;top:502px;width:46px;height:46px" role="img" aria-label="Photo of business professionals"></li>

    <li class="practice__item" style="top:586px">Company Law</li>
    <li class="practice__rule" style="top:605px"></li>
    <li class="practice__photo" style="left:353px;top:586px;width:58px;height:58px" role="img" aria-label="Photo of hands with a calculator and documents"></li>

    <li class="practice__item" style="top:675px">Wills and Estates</li>
    <li class="practice__rule" style="top:694px"></li>
    <li class="practice__photo" style="left:357px;top:673px;width:50px;height:50px" role="img" aria-label="Photo of an elderly couple"></li>

    <li class="practice__item" style="top:741px">Powers of Attorney and<br>Guardianship</li>
    <li class="practice__rule" style="top:781px"></li>
    <li class="practice__photo" style="left:353px;top:761px;width:58px;height:58px" role="img" aria-label="Photo of a carer with an elderly person"></li>
  </ul>
</section>

</body>
</html>
```